Advertising Material for Event

We are needing some advertising material done for an event. It can all be roughly the same except the two social media posts. We need:
- A banner
- A flyer
- 2 X social media posts

I have attached some examples of what we have done in the past. I have also attached a word document with the information.

Our colours are:
NAVY BLUE: Hex = #041E42 // RGB = 4 / 30 / 66 // CMYK = 100 / 90 / 13 / 68 // Pantone = 289 C
LIME GREEN: Hex = #97D700 // RGB = 151 / 215 / 0 // CMYK = 46 / 0 / 90 / 0 // Pantone = 375 C
WHITE

Our font are:
Avenir next regular, bold and demi bold
Freshman

Colors

Designer to choose colors to be used in the design.

Requirements
Must have
• Include photos provided. All info provided
Nice to have
• not cluttered

```html
<!DOCTYPE html>
<html lang="en">
<head>
<meta charset="utf-8">
<title>2022 Cheerleading Team Placements – Apex Gymsports</title>
<link rel="stylesheet" href="https://fonts.googleapis.com/css2?family=Alfa+Slab+One&family=Nunito+Sans:wght@300;400;700;800;900&display=swap">
<style>
  :root {
    --navy: #041E42;
    --navy-deep: #02142e;
    --lime: #97D700;
    --white: #ffffff;
    --photo-a: #2f4a2a;
    --photo-b: #7fae1c;
  }
  * { box-sizing: border-box; margin: 0; padding: 0; }
  html, body { width: 1200px; height: 1200px; overflow: hidden; background: var(--navy); }
  .poster {
    position: relative;
    width: 1200px;
    height: 1200px;
    overflow: hidden;
    background: radial-gradient(circle at 70% 20%, #0a2a57 0%, var(--navy) 55%, var(--navy-deep) 100%);
    font-family: "Nunito Sans", "Avenir Next", sans-serif;
    color: var(--white);
  }
  .backdrop, .stunt-photo { position: absolute; inset: 0; }
  .brand {
    position: absolute;
    left: 46px;
    top: 44px;
    display: flex;
    align-items: center;
    gap: 12px;
    font-family: "Nunito Sans", sans-serif;
    font-weight: 900;
    color: var(--lime);
    line-height: 1;
  }
  .brand-dot { width: 22px; height: 22px; border-radius: 50%; background: var(--lime); }
  .brand-name { font-size: 40px; letter-spacing: 1px; text-transform: uppercase; }
  .headline {
    position: absolute;
    right: 70px;
    top: 136px;
    text-align: right;
    font-family: "Alfa Slab One", "Freshman", serif;
    line-height: 1;
  }
  .headline-year { font-size: 90px; color: var(--white); }
  .headline-main { font-size: 88px; color: var(--lime); font-variant: small-caps; margin-top: 4px; letter-spacing: 1px; }
  .headline-sub { font-size: 70px; color: var(--white); font-variant: small-caps; margin-top: 12px; letter-spacing: 1px; }
  .intro {
    position: absolute;
    right: 70px;
    top: 404px;
    text-align: right;
    font-size: 19.5px;
    line-height: 25px;
    font-weight: 400;
  }
  .event-details {
    position: absolute;
    right: 70px;
    top: 493px;
    text-align: right;
    color: var(--lime);
    font-weight: 800;
    font-size: 39px;
    line-height: 46.5px;
  }
  .event-details sup { font-size: 22px; vertical-align: 16px; line-height: 0; }
  .price {
    position: absolute;
    right: 70px;
    top: 686px;
    text-align: right;
    font-family: "Alfa Slab One", serif;
    font-variant: small-caps;
    font-size: 26px;
    line-height: 31px;
  }
  .no-booking {
    position: absolute;
    right: 70px;
    top: 750px;
    font-size: 28px;
    font-weight: 300;
    text-transform: uppercase;
    letter-spacing: -0.3px;
  }
  .sessions {
    position: absolute;
    left: 614px;
    top: 793px;
    width: 519px;
    height: 77px;
    background: var(--lime);
    border-radius: 10px;
    display: flex;
    justify-content: space-around;
    align-items: center;
    color: var(--navy);
    font-weight: 800;
    font-size: 24px;
    line-height: 29px;
    text-align: center;
  }
  .notes {
    position: absolute;
    left: 638px;
    top: 918px;
    list-style: none;
    font-size: 22px;
    line-height: 24px;
    font-weight: 400;
  }
  .notes li { display: flex; gap: 14px; margin-bottom: 24px; }
  .notes svg { flex: none; width: 24px; height: 28px; margin-top: -4px; }
  .notes span { display: block; }
</style>
</head>
<body>
<main class="poster">
  <svg class="backdrop" width="1200" height="1200" viewBox="0 0 1200 1200" aria-hidden="true">
    <path d="M0 365 C260 380 520 600 600 1000 L640 1200 L0 1200 Z" fill="var(--lime)"/>
    <path d="M560 1200 C800 1170 1000 1175 1200 1122 L1200 1200 Z" fill="var(--lime)"/>
  </svg>

  <svg class="stunt-photo" width="1200" height="1200" viewBox="0 0 1200 1200" role="img" aria-label="Photo of a cheerleading team in navy and lime uniforms holding a flyer up in a stunt">
    <defs>
      <linearGradient id="stunt-tones" x1="0" y1="0" x2="0" y2="1">
        <stop offset="0" stop-color="var(--photo-b)" stop-opacity="0.85"/>
        <stop offset="0.5" stop-color="var(--navy-deep)" stop-opacity="0.9"/>
        <stop offset="1" stop-color="var(--photo-a)" stop-opacity="0.9"/>
      </linearGradient>
    </defs>
    <path d="M0 260 L290 160 L440 95 L520 130 L660 170 L640 330 L420 360 L460 560 L560 620 L610 760 L600 900 L560 1200 L60 1200 L70 560 L0 520 Z" fill="url(#stunt-tones)"/>
  </svg>

  <div class="brand">
    <span class="brand-dot"></span>
    <span class="brand-name">Apex Gymsports</span>
  </div>

  <h1 class="headline">
    <div class="headline-year">2022</div>
    <div class="headline-main">Cheerleading</div>
    <div class="headline-sub">Team placements</div>
  </h1>

  <p class="intro">Try out for a cheerleading team!<br>Everyone is welcome and will be placed on<br>a team, regardless of skill level.</p>

  <p class="event-details">Saturday<br>11<sup>th</sup> December 2021<br>Apex Gymsports, 14-16<br>Marlow Lane Eastwood</p>

  <p class="price">$10 and includes an Apex<br>merchandise pack</p>

  <p class="no-booking">No bookings required!</p>

  <div class="sessions">
    <div class="session">12 years and under<br>3:30-4:30pm</div>
    <div class="session">12 years and over<br>4:45-5:45pm</div>
  </div>

  <ul class="notes">
    <li>
      <svg viewBox="0 0 24 28" aria-hidden="true"><path d="M9 2 L17 8 L14 10 L15 16 L12 18 L8 13 L3 24 L2 23 L6 11 L2 7 L4 4 L10 6 Z" fill="var(--white)"/></svg>
      <span>Semi-competitive teams also available</span>
    </li>
    <li>
      <svg viewBox="0 0 24 28" aria-hidden="true"><path d="M9 2 L17 8 L14 10 L15 16 L12 18 L8 13 L3 24 L2 23 L6 11 L2 7 L4 4 L10 6 Z" fill="var(--white)"/></svg>
      <span>Current Apex Cheerleaders do not need to<br>attend placement day.</span>
    </li>
    <li>
      <svg viewBox="0 0 24 28" aria-hidden="true"><path d="M9 2 L17 8 L14 10 L15 16 L12 18 L8 13 L3 24 L2 23 L6 11 L2 7 L4 4 L10 6 Z" fill="var(--white)"/></svg>
      <span>If you cannot make placement day, contact<br>Apex to book a private placement.</span>
    </li>
  </ul>
</main>
</body>
</html>
```